Business cards/ stationery design for a transport consultancy
Freight Lantern
Business cards/ stationery design for a transport consultancy - Consulting
Creative Brief
Use standard fonts
Use either logo font (EUROSTILE LT STD) or complimentary font type
Simple
Declan Brolly
Managing Director
Ground Floor 27/ 28 Wexholm Yard Dublin 2 Ireland
dbrolly@freightlantern.com
www.freightlantern.com
Registered office address, and company registration number will need to be included as a footer at bottom of letter template.
Emphasis on designs should be on conveying a professional image.

```html
<!DOCTYPE html>
<html lang="en">
<head>
<meta charset="utf-8">
<title>Freight Lantern – Business Cards</title>
<link href="https://fonts.googleapis.com/css2?family=Michroma&family=Exo+2:wght@400;600&display=swap" rel="stylesheet">
<style>
  :root {
    --bg: #e9ebee;
    --blue-deep: #0d4f9a;
    --blue: #1b6fc4;
    --blue-light: #3f93e0;
    --grey: #8a8d91;
    --grey-dark: #4b4e52;
    --text: #2f3236;
    --white: #ffffff;
  }
  * { margin: 0; padding: 0; box-sizing: border-box; }
  html, body { width: 1200px; height: 864px; overflow: hidden; }
  body { background: var(--bg); position: relative; font-family: "Exo 2", sans-serif; }

  .card {
    position: absolute;
    width: 540px;
    height: 310px;
    border-radius: 18px;
    overflow: hidden;
    box-shadow: 0 6px 18px rgba(0,0,0,.18);
  }

  /* Front */
  .card-front {
    left: 50px; top: 170px;
    background: radial-gradient(ellipse at 55% 40%, var(--blue-light) 0%, var(--blue) 45%, var(--blue-deep) 100%);
  }
  .front-mark {
    position: absolute; left: 230px; top: 50px;
    width: 150px; height: 150px; border-radius: 50%;
    background: rgba(255,255,255,.08);
  }
  .front-name {
    position: absolute; left: 120px; top: 112px;
    font-family: "Michroma", sans-serif;
    color: var(--white);
    font-size: 30px; line-height: 1.15;
    letter-spacing: 1px;
    text-transform: uppercase;
  }

  /* Back */
  .card-back { left: 610px; top: 384px; background: var(--white); }
  .back-waves { position: absolute; left: 0; top: 0; width: 540px; height: 310px; }

  .brand {
    position: absolute; left: 30px; top: 40px;
    display: flex; align-items: center; gap: 12px;
  }
  .brand-dot { width: 34px; height: 34px; border-radius: 50%; background: var(--blue); }
  .brand-name {
    font-family: "Michroma", sans-serif;
    color: var(--blue); font-size: 17px; line-height: 1.2;
    text-transform: uppercase; letter-spacing: .5px;
  }

  .person { position: absolute; left: 30px; top: 130px; }
  .person-name { color: var(--blue); font-size: 12px; font-weight: 600; letter-spacing: 1.5px; text-transform: uppercase; }
  .person-role { color: var(--grey); font-size: 10px; letter-spacing: 1.5px; text-transform: uppercase; margin-top: 2px; }
  .person-address { color: var(--text); font-size: 10px; letter-spacing: 1.2px; text-transform: uppercase; margin-top: 14px; line-height: 1.5; }

  .contacts { position: absolute; left: 290px; top: 40px; list-style: none; }
  .contacts li {
    display: flex; align-items: center; gap: 8px;
    color: var(--text); font-size: 10.5px; letter-spacing: 1px;
    height: 17px;
  }
  .contact-icon {
    width: 12px; height: 12px; border-radius: 50%;
    background: var(--blue); flex: none;
    display: flex; align-items: center; justify-content: center;
  }
  .contact-icon svg { width: 8px; height: 8px; }
  .contact-divider { width: 1px; height: 72px; background: var(--grey); position: absolute; left: 280px; top: 40px; }
</style>
</head>
<body>

  <section class="card card-front" aria-label="Business card front">
    <div class="front-mark"></div>
    <div class="front-name">Freight<br>Lantern</div>
  </section>

  <section class="card card-back" aria-label="Business card back">
    <svg class="back-waves" viewBox="0 0 540 310" aria-hidden="true">
      <path d="M540,150 C430,220 300,275 90,310 L540,310 Z" fill="var(--grey)"/>
      <path d="M540,168 C440,235 320,285 140,310 L540,310 Z" fill="var(--grey-dark)"/>
      <path d="M540,190 C450,250 350,292 210,310 L540,310 Z" fill="var(--blue-light)"/>
      <path d="M540,205 C460,260 380,297 270,310 L540,310 Z" fill="var(--blue)"/>
    </svg>

    <div class="brand">
      <span class="brand-dot"></span>
      <span class="brand-name">Freight<br>Lantern</span>
    </div>

    <div class="contact-divider"></div>
    <ul class="contacts">
      <li><span class="contact-icon"><svg viewBox="0 0 10 10"><path d="M2 1 L4 1 L4.6 3 L3.5 3.8 Q4.5 5.8 6.2 6.5 L7 5.4 L9 6 L9 8 Q5 9 2.5 6 Q1 4 2 1Z" fill="#fff"/></svg></span>+353-1-555-0142</li>
      <li><span class="contact-icon"><svg viewBox="0 0 10 10"><rect x="3" y="1" width="4" height="8" rx="1" fill="#fff"/></svg></span>+353-87-555-0193</li>
      <li><span class="contact-icon"><svg viewBox="0 0 10 10"><rect x="1.5" y="2.5" width="7" height="5" fill="#fff"/><path d="M1.5 2.5 L5 5.5 L8.5 2.5" stroke="var(--blue)" stroke-width=".8" fill="none"/></svg></span>dbrolly@freightlantern.com</li>
      <li><span class="contact-icon"><svg viewBox="0 0 10 10"><circle cx="5" cy="5" r="3.5" stroke="#fff" stroke-width="1" fill="none"/><path d="M1.5 5 H8.5 M5 1.5 V8.5" stroke="#fff" stroke-width=".8"/></svg></span>www.freightlantern.com</li>
    </ul>

    <div class="person">
      <p class="person-name">Declan Brolly</p>
      <p class="person-role">Managing Director</p>
      <p class="person-address">Ground Floor 27/ 28 Wexholm Yard<br>Dublin 2 Ireland</p>
    </div>
  </section>

</body>
</html>
```